Real Estate Listing Signs for standard Yard arms

I need real estate listing signs done, for the standard sized sign to be hung beneath a white yard arm. To match existing logo. Information to be included:
-Logo
-Business name
-Phone number
-Marden Fosk Tundra Circle & Marden Fosk realty logos (smaller print)

Colors to be Red and anywhere in the gray scale between black and white, or a combination of those.

Target Market(s)

Drive by visuals

Industry/Entity Type

Real Estate Agent

Colors

Designer to choose only greyscale colors for use in the design.

Requirements
Must have
• My Logo and business name in same/similar font to whats provided, the MF tundra circle logo (small on bottom or corner somewhere), My phone number, and a decent amount of red coloration on the sign.

```html
<!DOCTYPE html>
<html lang="en">
<head>
<meta charset="utf-8">
<title>Brenlow Realty Yard Sign</title>
<link rel="stylesheet" href="https://fonts.googleapis.com/css2?family=Cinzel:wght@600;700&family=Oswald:wght@400&display=swap">
<style>
  :root {
    --sign-red: #ec2a35;
    --sign-black: #000000;
    --sign-grey: #e1e2e4;
    --sign-white: #ffffff;
  }
  html, body {
    margin: 0;
    padding: 0;
    width: 1200px;
    height: 894px;
    overflow: hidden;
    background: var(--sign-white);
  }
  .yard-sign {
    display: block;
    width: 1200px;
    height: 894px;
  }
  .band-black { fill: var(--sign-black); }
  .band-grey { fill: var(--sign-grey); }
  .field-red { fill: var(--sign-red); }
  .panel-white { fill: var(--sign-white); }
  .agent-name {
    font-family: "Cinzel", serif;
    font-weight: 600;
    font-size: 68px;
    fill: var(--sign-white);
  }
  .contact-phone, .contact-email {
    font-family: "Oswald", sans-serif;
    font-weight: 400;
    fill: var(--sign-red);
  }
  .contact-phone { font-size: 80px; }
  .contact-email { font-size: 62px; }
  .business-name {
    font-family: "Cinzel", serif;
    font-weight: 700;
    font-size: 66px;
    fill: var(--sign-black);
  }
  .brand-mark { fill: var(--sign-red); }
  .brokerage-name, .brokerage-sub, .office-notice {
    font-family: "Oswald", sans-serif;
    font-weight: 400;
    fill: var(--sign-white);
  }
  .brokerage-name { font-size: 44px; }
  .brokerage-sub { font-size: 22px; }
  .office-notice { font-size: 36px; }
</style>
</head>
<body>
<svg class="yard-sign" viewBox="0 0 1200 894" xmlns="http://www.w3.org/2000/svg">
  <!-- structure bands -->
  <rect class="band-black" x="0" y="0" width="1200" height="113"/>
  <rect class="band-grey" x="0" y="113" width="1200" height="140"/>
  <rect class="field-red" x="0" y="253" width="1200" height="489"/>
  <rect class="panel-white" x="128" y="267" width="944" height="461"/>
  <rect class="band-black" x="0" y="742" width="1200" height="152"/>

  <!-- central red ribbon -->
  <polygon class="field-red" points="536,113 665,233 665,253 536,253"/>
  <polygon class="field-red" points="536,267 665,267 665,352 600,288 536,352"/>
  <polygon class="field-red" points="536,658 600,723 665,658 665,742 536,742"/>
  <rect class="field-red" x="536" y="742" width="129" height="152"/>

  <!-- agent and contact -->
  <text class="agent-name" x="600" y="88" text-anchor="middle" textLength="623" lengthAdjust="spacingAndGlyphs">Jordan Brenlow</text>
  <text class="contact-phone" x="66" y="219" textLength="398" lengthAdjust="spacingAndGlyphs">907-555-0148</text>
  <text class="contact-email" x="670" y="205" textLength="483" lengthAdjust="spacingAndGlyphs">jbrenlow@mailbox.com</text>

  <!-- business identity -->
  <rect class="brand-mark" x="524" y="375" width="152" height="152"/>
  <text class="business-name" x="600" y="637" text-anchor="middle" textLength="580" lengthAdjust="spacingAndGlyphs">Brenlow Realty</text>

  <!-- brokerage -->
  <text class="brokerage-name" x="68" y="826" textLength="369" lengthAdjust="spacingAndGlyphs">MF TUNDRA CIRCLE</text>
  <text class="brokerage-sub" x="68" y="854" textLength="257" lengthAdjust="spacingAndGlyphs">MARDEN FOSK REALTY</text>

  <text class="office-notice" x="769" y="818" textLength="343" lengthAdjust="spacingAndGlyphs">Each Office Independently</text>
  <text class="office-notice" x="836" y="856" textLength="276" lengthAdjust="spacingAndGlyphs">Owned and Operated</text>
</svg>
</body>
</html>
```